Pawlume Tonic - Functtional water for dogs. Brand new product

I have a design alreday. It needs an upgrade. I need it in two steps. One that sums everything in 5 pges and one as the one as sent as the longer brief. So one that is a full version and one summary. I want it to be rea professional for a presentation to investors, stores etc. Important to make the same thur out the presentation so it feels like it belongs together. High end business but still modern for a brand new unique product. The first product on the market is Morning Brinefix (the other 3 mighgt come later on). Its in Sweden we start like a city like stockholm. Important that its realistic. Not to dark. Again think towards high end investors.

Target Market(s)

The presentation is for investors och businesses. The product is for dogowners who keep their animals as family members, active people, city people, people who travel etc

Industry/Entity Type

Dogs och dog food and vitamins

Requirements
Must have
• High end but still modern and breathe a brand new product thats unique. For investors that will invest money in this project.

```html
<!DOCTYPE html>
<html lang="en">
<head>
<meta charset="utf-8">
<title>Pawlume Tonic – Formula &amp; Ingredients</title>
<link rel="stylesheet" href="https://fonts.googleapis.com/css2?family=Syne:wght@600;700&family=Cabin:wght@400;500&display=swap">
<style>
  :root {
    --navy: #12283a;
    --card-bg: #13293a;
    --card-border: #3b5566;
    --teal: #14998a;
    --heading: #ffffff;
    --title: #e4ecf1;
    --body: #d6dee4;
    --art-cream: #f4efe4;
    --art-green: #7e9c6e;
    --art-tan: #c9925a;
  }
  * { margin: 0; padding: 0; box-sizing: border-box; }
  html, body {
    width: 1200px;
    height: 676px;
    overflow: hidden;
    background: var(--navy);
  }
  .slide {
    position: relative;
    width: 1200px;
    height: 676px;
    background: var(--navy);
    font-family: "Cabin", sans-serif;
    color: var(--body);
  }
  .slide-title {
    position: absolute;
    left: 154px;
    top: 30px;
    font-family: "Syne", sans-serif;
    font-weight: 700;
    font-size: 41px;
    letter-spacing: 0.2px;
    color: var(--heading);
  }
  .product-art {
    position: absolute;
    left: 154px;
    top: 127px;
    width: 523px;
    height: 297px;
    border-radius: 3px;
    background:
      radial-gradient(circle at 12% 80%, rgba(126,156,110,0.55), transparent 40%),
      radial-gradient(circle at 88% 65%, rgba(201,146,90,0.75), transparent 42%),
      radial-gradient(circle at 50% 45%, #ffffff, transparent 45%),
      linear-gradient(135deg, #efe6d4, var(--art-cream) 50%, #ead9bf);
  }
  .intro {
    position: absolute;
    left: 719px;
    top: 196px;
    width: 262px;
  }
  .intro-title {
    font-family: "Syne", sans-serif;
    font-weight: 600;
    font-size: 21px;
    color: var(--heading);
    margin-bottom: 16px;
  }
  .intro-text {
    font-size: 16px;
    line-height: 28px;
    color: var(--body);
  }
  .ingredients {
    position: absolute;
    left: 154px;
    top: 465px;
    display: flex;
    gap: 19px;
  }
  .ingredient-card {
    width: 263px;
    height: 185px;
    background: var(--card-bg);
    border: 1.5px solid var(--card-border);
    border-left: 6px solid var(--teal);
    border-radius: 2px;
    padding: 18px 20px 0 21px;
  }
  .ingredient-name {
    font-family: "Syne", sans-serif;
    font-weight: 600;
    font-size: 22px;
    color: var(--title);
    margin-bottom: 12px;
  }
  .ingredient-text {
    font-size: 16px;
    line-height: 28px;
    color: var(--body);
  }
</style>
</head>
<body>
  <main class="slide">
    <h1 class="slide-title">Formula &amp; Ingredients</h1>

    <div class="product-art" role="img" aria-label="Illustration of a Morning Brinefix jar surrounded by two dogs, leaves, berries and bowls of natural ingredients"></div>

    <section class="intro">
      <h2 class="intro-title">What's Inside</h2>
      <p class="intro-text">A clean, purposeful formula built on three core ingredients — each selected for proven physiological benefit in canine health.</p>
    </section>

    <section class="ingredients">
      <article class="ingredient-card">
        <h3 class="ingredient-name">Electrolytes</h3>
        <p class="ingredient-text">Replenish minerals lost through activity, heat, and stress. Support fluid uptake and cellular function.</p>
      </article>
      <article class="ingredient-card">
        <h3 class="ingredient-name">Minerals</h3>
        <p class="ingredient-text">Essential micronutrients that support muscle function, nerve signaling, and daily performance.</p>
      </article>
      <article class="ingredient-card">
        <h3 class="ingredient-name">Dextrose</h3>
        <p class="ingredient-text">Fast-acting glucose that accelerates fluid absorption and supports energy recovery after exertion.</p>
      </article>
    </section>
  </main>
</body>
</html>
```